Packaging Design: Logo/Bottle Design for New Botanical Cocktail Brand

We are a new start up, looking to create a new line of Ready to drink Cocktails. The brand name is Verdelle Garden Cocktails, infused with fruit, herb, and floral botanicals grown on our farm in New Hampshire. Flavors will include: Herb flavored with cilantro, Berry- flavored with Alpine Strawberry, Citrus flavored with lemon Verbena & lemon balm, Pear flavored with Bartlett pear, Cucumber & Mint. We need a logo and a label design. There are 2 possible bottles to choose from.

Designer has complete freedom with everything! From fonts and colors to bottle caps and closures. Please view the pinterest link for inspirational bottle designs. https://www.pinboardly.example/kestrawynn/garden-drinks/

Target Market(s)

Female 21 to 48 years old. College educated and professional. The type of person that has a passion for a cause and eats and shops local. People that respect an artisan quality product, hand made by a master craftsman.

Industry/Entity Type

Floral

Requirements
Must have
• Clear Bottle, see options attached. You may also choose your own BUT WE MUST SEE THE LOGO AND IMAGERY ON A BOTTLE
• Logo Design: "Verdelle Garden Cocktails"
• Label: We can have front and back, or one continuous label. We are open to painted designs.
• The label must contain the following text in quotes:
• Product Name: " Verdelle Garden Cocktails "
• "15% Alc. by Vol. (30 proof)"
• "750 mL"
• "Handcrafted and Bottled by Harrow Creek Orchard Farm and Distillery
• Winchester, NH-USA"
• The following Text must be in all caps and 3mm in height:
• "Government Warning: (1) According to the Surgeon General, women should not drink alcoholic beverages during pregnancy because of the risk of birth defects. (2) Consumption of alcoholic beverages impairs your ability to drive a car or operate machinery and may cause health problems."
• Must be a space for a bar code: .75 in height by 1.25 in length.
• “www.harrowcreekorchard.example”
• Must Have the following Statement:
• Infused with fruit, herb, and floral botanicals and sweetened with stevia. Serve cold over ice.
Nice to have
• Antique or vintage botanical illustrations
• https://www.pinboardly.example/kestrawynn/garden-drinks/
• check out the board for inspiration.
• Think artisanal small batch spirits that are ready to drink out of the bottle. Refreshing flavors just pour over ice and add herb leaves.
• You can use images by doing a search here.
• http://archive.plantrecords.example/search.xhtml?start=0&collectionFacet=Orchard+Fruit+Painting+Set

```html
<!DOCTYPE html>
<html lang="en">
<head>
<meta charset="utf-8">
<title>Verdelle Garden Cocktails — Pear Label</title>
<link href="https://fonts.googleapis.com/css2?family=Poiret+One&family=Josefin+Sans:wght@300&display=swap" rel="stylesheet">
<style>
  :root {
    --bg: #ecebe8;
    --label: #fbf9f4;
    --rule: #8c8784;
    --ink: #1e1c1b;
    --mauve: #8e6c64;
    --gold-top: #f3d08f;
    --gold-bottom: #e9ba68;
    --pear-light: #e8cf72;
    --pear-dark: #b98a3c;
    --leaf: #6f8a5a;
  }
  * { margin: 0; padding: 0; box-sizing: border-box; }
  html, body { width: 684px; height: 1200px; overflow: hidden; background: var(--bg); }
  .canvas { position: relative; width: 684px; height: 1200px; }

  .neck-band {
    position: absolute; left: 264px; top: 105px; width: 156px; height: 312px;
    background: linear-gradient(180deg, var(--gold-top), var(--gold-bottom));
    display: flex; align-items: center; justify-content: center;
  }
  .neck-band__name {
    font-family: "Poiret One", sans-serif; font-size: 30px; color: var(--mauve);
  }

  .main-label {
    position: absolute; left: 126px; top: 477px; width: 432px; height: 618px;
    background: var(--label);
  }
  .main-label__rules { position: absolute; inset: 0; }

  .flavor {
    position: absolute; top: 12px; width: 100%; text-align: center;
    font-family: "Josefin Sans", sans-serif; font-weight: 300;
    font-size: 20px; letter-spacing: 4px; color: var(--ink);
  }
  .botanical-art {
    position: absolute; left: 118px; top: 38px; width: 218px; height: 222px;
    border-radius: 45% 55% 50% 50%;
    background: radial-gradient(ellipse at 40% 62%, var(--pear-light) 0%, var(--pear-dark) 45%, var(--leaf) 72%, transparent 74%);
  }
  .brand-name {
    position: absolute; top: 268px; width: 100%; text-align: center;
    font-family: "Poiret One", sans-serif; font-size: 60px; color: var(--mauve);
  }
  .brand-block {
    position: absolute; left: 102px; top: 436px; width: 248px;
    text-align: center; font-family: "Poiret One", sans-serif;
    font-size: 31px; line-height: 44px; letter-spacing: 1.5px; color: var(--mauve);
  }
</style>
</head>
<body>
<div class="canvas">
  <div class="neck-band">
    <span class="neck-band__name">Verdelle</span>
  </div>

  <section class="main-label">
    <svg class="main-label__rules" width="432" height="618" viewBox="0 0 432 618" aria-hidden="true">
      <g stroke="#8c8784" stroke-width="1.4">
        <line x1="0" y1="1" x2="432" y2="1"/>
        <line x1="0" y1="198" x2="432" y2="198"/>
        <line x1="0" y1="416" x2="432" y2="416"/>
        <line x1="0" y1="617" x2="432" y2="617"/>
      </g>
      <g stroke="#6e6a68" stroke-width="2">
        <line x1="102" y1="0" x2="102" y2="4"/><line x1="350" y1="0" x2="350" y2="4"/>
        <line x1="102" y1="196" x2="102" y2="200"/><line x1="350" y1="196" x2="350" y2="200"/>
        <line x1="102" y1="414" x2="102" y2="418"/><line x1="350" y1="414" x2="350" y2="418"/>
        <line x1="102" y1="614" x2="102" y2="618"/><line x1="350" y1="614" x2="350" y2="618"/>
      </g>
      <rect x="102" y="416" width="248" height="201" fill="none" stroke="#e6e2dc" stroke-width="1"/>
    </svg>

    <div class="flavor">PEAR</div>
    <div class="botanical-art" role="img" aria-label="Vintage botanical illustration of a ripe pear on a stem with green leaves"></div>
    <div class="brand-name">Verdelle</div>
    <div class="brand-block">VERDELLE<br>GARDEN<br>COCKTAILS</div>
  </section>
</div>
</body>
</html>
```